Remote Planning & Scheduling Power Point Presentation

This PP presentation is to help explain what RPS is and its benefits. Need help with a better illustration on slide 3 that explains the process, overall aesthetics, need better images, and cleaner workflow on slide 18. Keep the DEW Logo in the bottom right of each slide. I have included a one-pager and infographic to help. I am still working of verbiage.

Thanks
SL

```html
<!DOCTYPE html>
<html lang="en">
<head>
<meta charset="utf-8">
<title>Remote Planning &amp; Scheduling – DEW Project Services</title>
<link href="https://fonts.googleapis.com/css2?family=Montserrat:wght@500;600;700;800&family=Open+Sans:wght@400;600&display=swap" rel="stylesheet">
<style>
:root{
  --navy:#1b3a8c;
  --navy-deep:#0f2a78;
  --red:#e0312b;
  --ink:#263042;
  --body:#4a5261;
  --muted:#8a909b;
  --canvas:#e6e9ee;
  --paper:#ffffff;
  --rule:#d5d9e0;
}
*{box-sizing:border-box;margin:0;padding:0}
html,body{width:1200px;height:4759px;overflow:hidden}
body{background:var(--canvas);font-family:"Open Sans",Arial,sans-serif;color:var(--body);position:relative}
.slide{position:absolute;width:562px;height:316px;background:var(--paper);box-shadow:0 2px 6px rgba(20,30,60,.18);overflow:hidden}
.slide.wide{width:1150px;height:644px}
.col-l{left:26px}.col-r{left:614px}
.slide-title{position:absolute;left:0;top:14px;border-left:6px solid var(--navy);padding-left:14px;font:700 18px/26px "Montserrat",sans-serif;color:var(--navy)}
.wide .slide-title{top:22px;border-left-width:10px;padding-left:26px;font-size:38px;line-height:60px}
.footer{position:absolute;left:0;right:0;bottom:0;height:40px;background:linear-gradient(#fff,#eef0f4)}
.footer .page{position:absolute;left:14px;top:18px;font-size:6px;color:var(--muted)}
.wide .footer{height:70px}
.wide .footer .page{left:40px;top:36px;font-size:13px}
.brand{position:absolute;right:16px;bottom:8px;font:800 20px/1 "Montserrat",sans-serif;color:var(--navy);letter-spacing:1px}
.wide .brand{right:34px;bottom:22px;font-size:36px}
.body{position:absolute;left:30px;top:62px;right:30px;font-size:9px;line-height:1.75;color:var(--body)}
.body ul{list-style:none}
.body li{padding-left:12px;position:relative}
.body li::before{content:"➢";position:absolute;left:0;color:#444}
.body ul ul{padding-left:14px}
.body ul ul li::before{content:"•"}
.body ul.ticks li::before{content:"✓"}
.body .gap{margin-top:10px}
.small{font-size:7px;line-height:1.8}
.tag-icon{position:absolute;right:24px;top:18px;width:40px;height:34px;border:1px solid var(--rule);border-radius:6px;background:#fff;box-shadow:0 1px 3px rgba(0,0,0,.12)}
.tag-icon svg{width:100%;height:100%}
.cover{color:#fff}
.cover.blue{background:linear-gradient(135deg,#2348b5 0%,#112d86 60%,#0a1e5e 100%)}
.cover.dark{background:linear-gradient(135deg,#3a3a3a 0%,#1e1e1e 60%,#0c0c0c 100%)}
.cover .scene{position:absolute;inset:0;opacity:.25;background:linear-gradient(180deg,transparent 40%,rgba(255,255,255,.35) 100%)}
.cover .logo{position:absolute;left:36px;top:70px;font:800 50px/1 "Montserrat",sans-serif;color:#fff;letter-spacing:2px}
.cover .sub{position:absolute;left:40px;top:128px;font:600 8px "Montserrat",sans-serif;letter-spacing:1px}
.cover .heading{position:absolute;left:40px;top:222px;border-left:3px solid #fff;padding-left:14px;font:700 18px/1.5 "Montserrat",sans-serif}
.cover .heading small{display:block;font-size:8px}
.panel{position:absolute;left:0;right:0;top:56px;bottom:40px;background:var(--navy-deep);color:#fff;font-size:8.5px;line-height:1.9;padding:26px 40px}
.panel ul{list-style:none}
.panel li{padding-left:12px;position:relative}
.panel li::before{content:"➢";position:absolute;left:0}
.panel ul.ticks li::before{content:"✓"}
.node{position:absolute;width:148px;height:92px;background:#fff;border-radius:14px;box-shadow:0 3px 10px rgba(20,30,60,.22);text-align:center;font:500 14px/1.15 "Open Sans",sans-serif;color:var(--ink);padding-top:50px}
.node .ico{position:absolute;left:46px;top:-16px;width:56px;height:56px;border-radius:50%;background:#fff;border:3px solid var(--navy);box-shadow:0 2px 5px rgba(0,0,0,.2)}
.node.hot .ico{border-color:var(--red)}
.node .ico svg{width:100%;height:100%}
.level3{position:absolute;left:1072px;top:430px;width:48px;height:48px;border-radius:50%;border:3px solid #777;background:#fff}
.level3-label{position:absolute;left:1058px;top:482px;width:80px;text-align:center;font-size:14px;line-height:1.1;color:var(--ink)}
.photo{position:absolute;border:2px solid #fff;box-shadow:0 2px 6px rgba(0,0,0,.3)}
.cap{position:absolute;text-align:center;font-size:18px;color:var(--ink)}
.task-box{position:absolute;left:104px;top:363px;width:259px;height:138px;border:3px solid var(--navy);border-radius:8px;background:#fff;text-align:center;font-size:17px;line-height:1.3;color:var(--ink);padding-top:18px;box-shadow:0 2px 6px rgba(0,0,0,.2)}
.chip{position:absolute;right:50px;top:28px;border:2px solid #888;border-radius:6px;padding:6px 16px;font:700 20px "Montserrat",sans-serif;color:var(--ink);box-shadow:0 2px 4px rgba(0,0,0,.2)}
</style>
</head>
<body>

<section class="slide cover blue col-l" style="top:26px">
  <div class="scene" role="img" aria-label="Faded industrial plant and mountains backdrop"></div>
  <div class="logo">DEW</div><div class="sub">PROJECT SERVICES, LTD.</div>
  <div class="heading">Remote Planning &amp; Scheduling<small>2020</small></div>
</section>
<section class="slide cover dark col-r" style="top:26px">
  <div class="scene" role="img" aria-label="Faded industrial plant and mountains backdrop"></div>
  <div class="logo">DEW</div><div class="sub">PROJECT SERVICES, LTD.</div>
  <div class="heading">Remote Planning &amp; Scheduling<small>2020</small></div>
</section>

<section class="slide col-l" style="top:364px">
  <h2 class="slide-title">Innovative Approach to Planning</h2>
  <div class="body"><ul>
    <li>No more paying for man hours, buy a finished product</li>
    <li>Able to focus on getting the right scope, let us focus on your planning</li>
  </ul></div>
  <footer class="footer"><span class="page">2 &nbsp;|&nbsp; Copyright © 2020 DEW Project Services, Ltd. | All Rights Reserved</span><span class="brand">DEW</span></footer>
</section>
<section class="slide col-r" style="top:364px">
  <h2 class="slide-title">RPS Flow Process</h2>
  <svg width="562" height="276" viewBox="0 0 562 276" style="position:absolute;left:0;top:40px" font-family="Open Sans, sans-serif" font-size="4.5" text-anchor="middle">
    <g stroke="#999" stroke-dasharray="2 2" fill="none">
      <path d="M82 41H128M180 41H226M278 41H324M376 41H423"/>
      <path d="M475 41C510 41 510 115 475 115"/>
      <path d="M128 115H82M226 115H180M324 115H278M423 115H376"/>
      <path d="M30 115C0 115 0 189 30 189"/>
      <path d="M82 189H128M180 189H226M278 189H324M376 189H423M475 189H500"/>
    </g>
    <g>
      <rect x="30" y="22" width="52" height="38" rx="6" fill="#1b3a8c"/>
      <rect x="128" y="22" width="52" height="38" rx="6" fill="#1b3a8c"/>
      <rect x="226" y="22" width="52" height="38" rx="6" fill="#1b3a8c"/>
      <rect x="324" y="22" width="52" height="38" rx="6" fill="#1b3a8c"/>
      <rect x="423" y="22" width="52" height="38" rx="6" fill="#1b3a8c"/>
      <rect x="30" y="96" width="52" height="38" rx="6" fill="#e0312b"/>
      <rect x="128" y="96" width="52" height="38" rx="6" fill="#e0312b"/>
      <rect x="226" y="96" width="52" height="38" rx="6" fill="#e0312b"/>
      <rect x="324" y="96" width="52" height="38" rx="6" fill="#e0312b"/>
      <rect x="423" y="96" width="52" height="38" rx="6" fill="#1b3a8c"/>
      <rect x="30" y="170" width="52" height="38" rx="6" fill="#1b3a8c"/>
      <rect x="128" y="170" width="52" height="38" rx="6" fill="#e0312b"/>
      <rect x="226" y="170" width="52" height="38" rx="6" fill="#1b3a8c"/>
      <rect x="324" y="170" width="52" height="38" rx="6" fill="#e0312b"/>
      <rect x="423" y="170" width="52" height="38" rx="6" fill="#1b3a8c"/>
    </g>
    <g fill="none" stroke="#fff" stroke-width=".8">
      <circle cx="56" cy="34" r="7"/><circle cx="154" cy="34" r="7"/><circle cx="252" cy="34" r="7"/><circle cx="350" cy="34" r="7"/><circle cx="449" cy="34" r="7"/>
      <circle cx="56" cy="108" r="7"/><circle cx="154" cy="108" r="7"/><circle cx="252" cy="108" r="7"/><circle cx="350" cy="108" r="7"/><circle cx="449" cy="108" r="7"/>
      <circle cx="56" cy="182" r="7"/><circle cx="154" cy="182" r="7"/><circle cx="252" cy="182" r="7"/><circle cx="350" cy="182" r="7"/><circle cx="449" cy="182" r="7"/>
    </g>
    <g fill="#fff">
      <text x="56" y="53">On Site</text><text x="154" y="53">Collect Work list</text><text x="252" y="53">Scope Review</text><text x="350" y="53">Planning Premise</text><text x="449" y="53">Data Collection</text>
      <text x="56" y="127">Package Review</text><text x="154" y="127">Develop Package</text><text x="252" y="127">Detail Planning</text><text x="350" y="127">Remote</text><text x="449" y="127">Field Photos</text>
      <text x="56" y="199">Package</text><text x="56" y="204">Acceptance</text><text x="154" y="201">Level 1</text><text x="252" y="201">Schedule Review</text><text x="350" y="201">Level 2</text><text x="449" y="201">Schedule Review</text>
    </g>
    <circle cx="512" cy="180" r="12" fill="#fff" stroke="#777" stroke-width="1.5"/>
    <text x="512" y="201" fill="#333">Level 3</text><text x="512" y="206" fill="#333">Schedule</text>
  </svg>
  <footer class="footer"><span class="page">4 &nbsp;|&nbsp; Copyright © 2020 DEW Project Services, Ltd. | All Rights Reserved</span><span class="brand">DEW</span></footer>
</section>

<section class="slide wide" style="left:26px;top:704px">
  <h2 class="slide-title">RPS Flow Process</h2>
  <svg width="1150" height="644" viewBox="0 0 1150 644" style="position:absolute;left:0;top:0">
    <defs><marker id="arrowhead" markerWidth="8" markerHeight="8" refX="6" refY="4" orient="auto"><path d="M0 0L8 4L0 8z" fill="#666"/></marker></defs>
    <g stroke="#666" stroke-width="2" stroke-dasharray="4 4" fill="none" marker-end="url(#arrowhead)">
      <path d="M215 174H266"/><path d="M418 174H466"/><path d="M618 174H664"/><path d="M816 174H863"/>
      <path d="M1015 174C1100 174 1100 322 1019 322"/>
      <path d="M867 322H820"/><path d="M668 322H622"/><path d="M470 322H422"/><path d="M270 322H219"/>
      <path d="M67 322C-10 322 -10 470 63 470"/>
      <path d="M215 470H266"/><path d="M418 470H466"/><path d="M618 470H664"/><path d="M816 470H863"/><path d="M1015 470H1066"/>
    </g>
  </svg>
  <div class="node" style="left:67px;top:128px"><span class="ico"><svg viewBox="0 0 50 50"><g fill="none" stroke="#1b3a8c" stroke-width="2"><circle cx="17" cy="20" r="4"/><circle cx="25" cy="18" r="4"/><circle cx="33" cy="20" r="4"/><path d="M11 34c0-6 12-6 12 0M19 32c0-7 12-7 12 0M27 34c0-6 12-6 12 0"/></g></svg></span>On Site</div>
  <div class="node" style="left:270px;top:128px"><span class="ico"><svg viewBox="0 0 50 50"><g fill="none" stroke="#1b3a8c" stroke-width="2"><rect x="15" y="12" width="20" height="26" rx="2"/><path d="M19 19h12M19 24h12M19 29h8"/></g></svg></span>Collect Work list</div>
  <div class="node" style="left:470px;top:128px"><span class="ico"><svg viewBox="0 0 50 50"><g fill="none" stroke="#1b3a8c" stroke-width="2.5"><circle cx="22" cy="22" r="9"/><path d="M29 29l8 8"/></g></svg></span>Scope Review</div>
  <div class="node" style="left:668px;top:128px"><span class="ico"><svg viewBox="0 0 50 50"><g fill="none" stroke="#1b3a8c" stroke-width="2"><rect x="14" y="13" width="22" height="24" rx="2"/><path d="M18 20h14M18 25h14M18 30h9"/></g></svg></span>Planning Premise</div>
  <div class="node" style="left:867px;top:128px"><span class="ico"><svg viewBox="0 0 50 50"><g fill="none" stroke="#1b3a8c" stroke-width="2"><rect x="14" y="13" width="22" height="7" rx="1"/><rect x="14" y="22" width="22" height="7" rx="1"/><rect x="14" y="31" width="22" height="7" rx="1"/></g></svg></span>Data Collection</div>
  <div class="node hot" style="left:67px;top:276px"><span class="ico"><svg viewBox="0 0 50 50"><g fill="none" stroke="#e0312b" stroke-width="2"><rect x="13" y="12" width="18" height="24" rx="2"/><circle cx="30" cy="29" r="6"/><path d="M34 33l5 5"/></g></svg></span>Package Review</div>
  <div class="node hot" style="left:270px;top:276px"><span class="ico"><svg viewBox="0 0 50 50"><g fill="none" stroke="#e0312b" stroke-width="2"><circle cx="21" cy="22" r="6"/><circle cx="31" cy="31" r="5"/><path d="M21 12v4M21 28v4M11 22h4M27 22h4"/></g></svg></span>Develop Package</div>
  <div class="node hot" style="left:470px;top:276px"><span class="ico"><svg viewBox="0 0 50 50"><g fill="none" stroke="#e0312b" stroke-width="2"><rect x="14" y="13" width="22" height="24" rx="2"/><path d="M18 19h6v6h-6zM27 20h6M27 24h6M18 30h15"/></g></svg></span>Detail Planning</div>
  <div class="node hot" style="left:668px;top:276px"><span class="ico"><svg viewBox="0 0 50 50"><g fill="none" stroke="#e0312b" stroke-width="2"><circle cx="25" cy="25" r="3"/><path d="M18 18a10 10 0 0 0 0 14M32 18a10 10 0 0 1 0 14M14 14a16 16 0 0 0 0 22M36 14a16 16 0 0 1 0 22"/></g></svg></span>Remote</div>
  <div class="node" style="left:867px;top:276px"><span class="ico"><svg viewBox="0 0 50 50"><g fill="none" stroke="#1b3a8c" stroke-width="2"><rect x="12" y="18" width="26" height="18" rx="2"/><circle cx="25" cy="27" r="5"/><path d="M19 18l3-4h6l3 4"/></g></svg></span>Field Photos</div>
  <div class="node" style="left:67px;top:424px;padding-top:44px"><span class="ico"><svg viewBox="0 0 50 50"><g fill="none" stroke="#1b3a8c" stroke-width="2"><path d="M12 24l7-6 6 4 6-4 7 6-10 9z"/><path d="M19 27l5 5M23 25l5 5"/></g></svg></span>Package<br>Acceptance</div>
  <div class="node hot" style="left:270px;top:424px"><span class="ico"><svg viewBox="0 0 50 50"><g fill="none" stroke="#e0312b" stroke-width="2"><rect x="13" y="15" width="24" height="22" rx="2"/><path d="M13 21h24M19 12v6M31 12v6M18 26h3M24 26h3M30 26h3M18 31h3M24 31h3"/></g></svg></span>Level 1</div>
  <div class="node" style="left:470px;top:424px"><span class="ico"><svg viewBox="0 0 50 50"><g fill="none" stroke="#1b3a8c" stroke-width="2"><rect x="14" y="12" width="22" height="26" rx="2"/><circle cx="25" cy="22" r="4"/><path d="M18 34c0-6 14-6 14 0"/></g></svg></span>Schedule Review</div>
  <div class="node hot" style="left:668px;top:424px"><span class="ico"><svg viewBox="0 0 50 50"><g fill="none" stroke="#e0312b" stroke-width="2"><rect x="13" y="15" width="24" height="22" rx="2"/><path d="M13 21h24M19 12v6M31 12v6M18 26h3M24 26h3M30 26h3M18 31h3M24 31h3"/></g></svg></span>Level 2</div>
  <div class="node" style="left:867px;top:424px"><span class="ico"><svg viewBox="0 0 50 50"><g fill="none" stroke="#1b3a8c" stroke-width="2"><rect x="14" y="12" width="22" height="26" rx="2"/><circle cx="25" cy="22" r="4"/><path d="M18 34c0-6 14-6 14 0"/></g></svg></span>Schedule Review</div>
  <div class="level3"><svg viewBox="0 0 42 42" width="42" height="42"><g fill="none" stroke="#777" stroke-width="2"><rect x="11" y="12" width="20" height="18" rx="2"/><path d="M11 17h20M16 10v4M26 10v4"/></g></svg></div>
  <div class="level3-label">Level 3<br>Schedule</div>
  <footer class="footer"><span class="page">5 &nbsp;|&nbsp; Copyright © 2020 DEW Project Services, Ltd. | All Rights Reserved</span><span class="brand">DEW</span></footer>
</section>

<section class="slide col-l" style="top:1372px">
  <h2 class="slide-title">Detail Planning</h2>
  <div class="tag-icon"><svg viewBox="0 0 40 34"><g fill="none" stroke="#e0312b" stroke-width="1.5"><rect x="12" y="7" width="16" height="20" rx="1"/><path d="M15 12h5v5h-5zM22 13h4M15 21h10"/></g></svg></div>
  <div class="body small" style="top:66px"><ul>
    <li>Conducted field walk &amp; captured field notes</li>
    <li>Collected field photos</li>
    <li>Create job activities, identify resources, estimate durations, identify TA phases</li>
    <li>Annotate pictures and P&amp;ID's</li>
    <li>Identify blind points (hydro, &amp; entry blinds)</li>
    <li>Identify PPE requirements</li>
    <li>Provide safety ranking for each activity</li>
    <li>Create material list</li>
    <li>Create job packages</li>
    <li>Capture notes at the activity level</li>
    <li>Scaffold Requirements</li>
  </ul></div>
  <footer class="footer"><span class="page">6 &nbsp;|&nbsp; Copyright © 2020 DEW Project Services, Ltd. | All Rights Reserved</span><span class="brand">DEW</span></footer>
</section>
<section class="slide col-r" style="top:1372px">
  <h2 class="slide-title">Develop Package</h2>
  <div class="tag-icon"><svg viewBox="0 0 40 34"><g fill="none" stroke="#e0312b" stroke-width="1.5"><circle cx="18" cy="15" r="5"/><circle cx="26" cy="22" r="4"/><path d="M18 7v3M18 20v3M10 15h3M23 15h3"/></g></svg></div>
  <div class="body small" style="top:84px;display:flex;gap:26px">
    <ul style="flex:1">
      <li>P&amp;ID - mark up scope &amp; blind location</li>
      <li>Plot Plan - mark up scope</li>
      <li>Equip Dwgs – collect add to package</li>
      <li>Equip Data Sheet - collect add to package</li>
      <li>Photo - mark up and scope description</li>
      <li>Safety Data Sheet - identify PPE required</li>
      <li>Step Out - create job step out</li>
      <li>Blind List - create blind list</li>
    </ul>
    <ul style="flex:1">
      <li>Material List - create material list</li>
      <li>QAQC Forms - fill out planning information</li>
      <li>Closure Forms - fill out planning information</li>
      <li>Spec Sheets - order material according to spec</li>
      <li>ITP - incorporate ITP in job plans</li>
      <li>Safety Risk - identify risk level</li>
      <li>MI Reports - fill out planning information</li>
    </ul>
  </div>
  <footer class="footer"><span class="page">7 &nbsp;|&nbsp; Copyright © 2020 DEW Project Services, Ltd. | All Rights Reserved</span><span class="brand">DEW</span></footer>
</section>

<section class="slide col-l" style="top:1712px">
  <h2 class="slide-title">Package Review</h2>
  <div class="tag-icon"><svg viewBox="0 0 40 34"><g fill="none" stroke="#e0312b" stroke-width="1.5"><rect x="12" y="7" width="13" height="18" rx="1"/><circle cx="24" cy="20" r="4"/><path d="M27 23l4 4"/></g></svg></div>
  <footer class="footer"><span class="page">8 &nbsp;|&nbsp; Copyright © 2020 DEW Project Services, Ltd. | All Rights Reserved</span><span class="brand">DEW</span></footer>
</section>
<section class="slide col-r" style="top:1712px">
  <h2 class="slide-title">Package Acceptance</h2>
  <div class="tag-icon"><svg viewBox="0 0 40 34"><g fill="none" stroke="#1b3a8c" stroke-width="1.5"><path d="M9 16l6-5 5 3 5-3 6 5-11 8z"/></g></svg></div>
  <footer class="footer"><span class="page">9 &nbsp;|&nbsp; Copyright © 2020 DEW Project Services, Ltd. | All Rights Reserved</span><span class="brand">DEW</span></footer>
</section>

<section class="slide col-l" style="top:2052px">
  <h2 class="slide-title">Schedules</h2>
  <div class="tag-icon"><svg viewBox="0 0 40 34"><g fill="none" stroke="#555" stroke-width="1.5"><rect x="10" y="8" width="20" height="18" rx="1"/><path d="M10 13h20M14 17h3M19 17h3M24 17h3M14 21h3M19 21h3M24 21h3"/></g></svg></div>
  <svg width="150" height="150" viewBox="0 0 150 150" style="position:absolute;left:40px;top:88px" font-family="Montserrat, sans-serif" font-size="8" font-weight="700" fill="#fff">
    <path d="M0 2H112L124 14L112 26H0z" fill="#1b3a8c"/><text x="6" y="17">Level 1</text>
    <path d="M0 40H112L124 52L112 64H0z" fill="#1b3a8c"/><text x="6" y="55">Level 2</text>
    <path d="M0 78H112L124 90L112 102H0z" fill="#1b3a8c"/><text x="6" y="93">Level 3</text>
    <path d="M0 116H112L124 128L112 140H0z" fill="#e0312b"/><text x="6" y="131">Schedule Reviews</text>
  </svg>
  <div class="body" style="left:218px;top:52px;font-size:6.5px;line-height:2.1"><ul>
    <li>Internal Logic as well as external logic</li>
    <li>Resource leveling</li>
    <li>Histograms</li>
    <li>Milestone KPI's</li>
    <li>Customized Reporting</li>
    <li>Risk Reviewed</li>
    <li>Internal Logic only, from one Task to another e.g..... Blind Exchanger to Open Dollar Plate etc....)</li>
    <li>Resource loaded Tasks</li>
    <li>Standard Activity Codes assigned to all Tasks</li>
    <li>Default Calendars assigned to all Activities (8 hours per day, 5 Days per Week) unless prearranged to use a TAR calendar as the default</li>
    <li>All following PMCORE rules for project development</li>
  </ul></div>
  <footer class="footer"><span class="page">10 &nbsp;|&nbsp; Copyright © 2020 DEW Project Services, Ltd. | All Rights Reserved</span><span class="brand">DEW</span></footer>
</section>
<section class="slide col-r" style="top:2052px">
  <h2 class="slide-title">Remote Planning &amp; Scheduling¹</h2>
  <div class="body" style="top:64px"><ul>
    <li>Increase efficiency in resource utilization
      <ul><li>Share resources between facilities and events</li><li>Standardize processes across all sites</li></ul></li>
    <li class="gap">Build customizable code structures into the job plans</li>
    <li>Build safety into each plan</li>
    <li>Transparent</li>
    <li>Measurable</li>
    <li>Accountable</li>
  </ul></div>
  <footer class="footer"><span class="page">11 &nbsp;|&nbsp; Copyright © 2020 DEW Project Services, Ltd. | All Rights Reserved</span><span class="brand">DEW</span></footer>
</section>

<section class="slide col-l" style="top:2391px">
  <h2 class="slide-title">Remote Planning &amp; Scheduling²</h2>
  <div class="body" style="top:64px"><ul>
    <li>Reduce and contain cost of planning
      <ul><li>Reduce/eliminate per diem, overtime</li><li>Reduce headcount on site</li></ul></li>
    <li class="gap">Reduces facilities requirements and safety exposure</li>
    <li>Fixed cost per work package/lump sum</li>
    <li>Enforces compliance with FEL deliverables</li>
    <li>Drive consistency in turnaround processes</li>
  </ul></div>
  <footer class="footer"><span class="page">12 &nbsp;|&nbsp; Copyright © 2020 DEW Project Services, Ltd. | All Rights Reserved</span><span class="brand">DEW</span></footer>
</section>
<section class="slide col-r" style="top:2391px">
  <h2 class="slide-title">Concept: Using the Best!</h2>
  <div class="body" style="top:72px;font-size:6.8px;line-height:2.6"><ul>
    <li>Schedulers housed in the DEW corporate office in Port Marlow</li>
    <li>Schedulers with access to the latest "Tested" version of Tempora</li>
    <li>Schedulers have access to skills training, Tempora/Vantix Pulse</li>
    <li>Schedulers have access to SME's for schedule "pier out" at anytime during development of their schedule</li>
    <li>Schedulers with the skill set to host meetings at the site via telecom (video conferencing) software</li>
    <li>Schedulers that are certified as Lead schedulers, all the way to Master Schedulers under DEW</li>
    <li>Full time or part time schedulers</li>
    <li>No travel, No overtime, scalable work hours per week or month</li>
  </ul></div>
  <footer class="footer"><span class="page">13 &nbsp;|&nbsp; Copyright © 2020 DEW Project Services, Ltd. | All Rights Reserved</span><span class="brand">DEW</span></footer>
</section>

<section class="slide col-l" style="top:2731px">
  <h2 class="slide-title">Savings</h2>
  <div class="panel" style="font-size:8px;line-height:2.1"><ul>
    <li>Pay for the time/Package you use</li><li>No Per Diem</li><li>No Overtime</li><li>No Paid Holidays</li><li>No Sick Leave</li><li>No Vacations Hours</li><li>No Taxes</li><li>No Insurance</li><li>No Risk</li><li>No Safety Site Classes and No Background Checks to Perform</li>
  </ul></div>
  <footer class="footer"><span class="page">14 &nbsp;|&nbsp; Copyright © 2020 DEW Project Services, Ltd. | All Rights Reserved</span><span class="brand">DEW</span></footer>
</section>
<section class="slide col-r" style="top:2731px">
  <h2 class="slide-title">Packages: Planning Phase</h2>
  <div class="body" style="top:68px;font-size:6.8px;line-height:2.4"><ul>
    <li>Standard Package
      <ul style="list-style:none"><li>1. &nbsp;Schedule Weekly Progress Report Contains the Following:
        <ul><li>Start Date of Schedule Development<ul class="ticks"><li>Assign a Start Data Date</li></ul></li>
        <li>Number of Worklist Item in Schedule</li><li>Worklist Items in Schedule with Details (Tasks) added</li><li>Logic % Complete</li><li>Worklist Items with Resources and all Activity Codes Progress</li><li>Trended Completion Date</li></ul></li></ul></li>
  </ul></div>
  <footer class="footer"><span class="page">15 &nbsp;|&nbsp; Copyright © 2020 DEW Project Services, Ltd. | All Rights Reserved</span><span class="brand">DEW</span></footer>
</section>

<section class="slide col-l" style="top:3071px">
  <h2 class="slide-title">Packages: Planning Phase</h2>
  <div class="body" style="top:68px;font-size:6.8px;line-height:2.4"><ul>
    <li>Standard Package:
      <ul><li>Internal Logic only, from one Task to another e.g..... Blind Exchanger to Open Dollar Plate etc....)</li><li>Resource loaded Tasks</li><li>Standard Activity Codes assigned to all Tasks</li><li>Default Calendars assigned to all Activities (8 hours per day, 5 Days per Week) unless prearranged to use a TAR calendar as the default</li><li>All following PMCORE rules for project development</li></ul></li>
  </ul></div>
  <footer class="footer"><span class="page">16 &nbsp;|&nbsp; Copyright © 2020 DEW Project Services, Ltd. | All Rights Reserved</span><span class="brand">DEW</span></footer>
</section>
<section class="slide col-r" style="top:3071px">
  <h2 class="slide-title">Packages: Planning Phase</h2>
  <div class="body" style="top:68px;font-size:6.8px;line-height:2.4"><ul>
    <li>Advanced Package:
      <ul style="list-style:none"><li>1. &nbsp;All the Standard Package items plus:
        <ul><li>Internal Logic as well as external logic</li><li>Resource leveling</li><li>Histograms</li><li>Milestone KPI's</li><li>Customized Reporting</li><li>Risk Reviewed</li></ul></li></ul></li>
  </ul></div>
  <footer class="footer"><span class="page">17 &nbsp;|&nbsp; Copyright © 2020 DEW Project Services, Ltd. | All Rights Reserved</span><span class="brand">DEW</span></footer>
</section>

<section class="slide col-l" style="top:3411px">
  <h2 class="slide-title">Conclusion</h2>
  <div class="body" style="top:66px;font-size:8.5px;line-height:2"><ul class="ticks">
    <li>Remote Planning/Scheduling we save your organization from the headaches and troubles of finding the right person for the right job. Cut your expenses of housing the new employee as well as the reduced overhead cost</li>
  </ul></div>
  <footer class="footer"><span class="page">18 &nbsp;|&nbsp; Copyright © 2020 DEW Project Services, Ltd. | All Rights Reserved</span><span class="brand">DEW</span></footer>
</section>
<section class="slide col-r" style="top:3411px">
  <h2 class="slide-title">Leveraging the Industries Best</h2>
  <div class="body" style="top:72px;right:300px;font-size:6.8px;line-height:1.6"><ul>
    <li style="margin-bottom:10px">DEW's office is located in Port Marlow, right in the heart of the Petro-Chemical and Refining industry.</li>
    <li style="margin-bottom:10px">We have access to many of the skilled resources needed for STO planning.</li>
    <li style="margin-bottom:10px">This also eliminates paying per diem cost, no more temporary offices, no more overtime.</li>
    <li>Remote Planning also offers fixed prices, now you know how much planning will cost before getting started.</li>
  </ul></div>
  <div style="position:absolute;left:276px;top:72px;width:1px;height:170px;background:var(--rule)"></div>
  <div role="img" aria-label="Map of the country in flag colours with a refinery pipe rack" style="position:absolute;left:306px;top:74px;width:230px;height:150px;border-radius:40% 30% 45% 35%;background:linear-gradient(135deg,#2c4aa6 0%,#c7cbe0 50%,#d33a3a 100%)"></div>
  <footer class="footer"><span class="page">19 &nbsp;|&nbsp; Copyright © 2020 DEW Project Services, Ltd. | All Rights Reserved</span><span class="brand">DEW</span></footer>
</section>

<section class="slide wide" style="left:26px;top:3750px">
  <h2 class="slide-title">Keeping Everyone Connected</h2>
  <div class="chip">Remote Planning</div>
  <div class="photo" role="img" aria-label="Leadership team meeting around a table" style="left:104px;top:128px;width:259px;height:135px;background:linear-gradient(135deg,#c7b59a,#6d5d4e)"></div>
  <div class="cap" style="left:104px;top:270px;width:259px">Leadership Team</div>
  <div class="photo" role="img" aria-label="Planner on site at an industrial plant" style="left:431px;top:128px;width:259px;height:135px;background:linear-gradient(135deg,#8aa0b8,#2d3b50)"></div>
  <div class="cap" style="left:431px;top:270px;width:259px">On Site Planner</div>
  <div class="photo" role="img" aria-label="Screenshot of a complete work package document" style="left:777px;top:128px;width:256px;height:135px;background:linear-gradient(135deg,#f2f4f8,#b9c3d6)"></div>
  <div class="cap" style="left:777px;top:270px;width:256px">Complete Work Package</div>
  <div class="task-box">Monitor Progress<br>Review Content<br>Track FEL Assignments<br>Develop Budgets<br>Share with Stakeholders</div>
  <div class="photo" role="img" aria-label="Planning software dashboard on a monitor" style="left:446px;top:359px;width:231px;height:140px;background:linear-gradient(135deg,#3b4552,#1a2230)"></div>
  <div class="cap" style="left:446px;top:506px;width:231px">SITEplanner</div>
  <div class="photo" role="img" aria-label="Remote planner team working at computers in an office" style="left:762px;top:359px;width:261px;height:140px;background:linear-gradient(135deg,#d9dde4,#7f8a9b)"></div>
  <div class="cap" style="left:762px;top:506px;width:261px">Remote Planner Team</div>
  <svg class="connectors" width="1150" height="644" viewBox="0 0 1150 644" style="position:absolute;left:0;top:0" fill="#e0312b">
    <path d="M378 195l13-11v7h22v-7l13 11-13 11v-7h-22v7z"/>
    <path d="M712 195l14-12v7h22v10h-22v7z"/>
    <path d="M233 302l-12 14h7v22h10v-22h7z"/>
    <path d="M561 352l-12-14h7v-22h10v22h7z"/>
    <path d="M903 302l-12 14h7v22h10v-22h7z"/>
    <path d="M380 430l14-12v7h22v10h-22v7z"/>
    <path d="M748 430l-14-12v7h-22v10h22v7z"/>
  </svg>
  <footer class="footer"><span class="page">20 &nbsp;|&nbsp; Copyright © 2020 DEW Project Services, Ltd. | All Rights Reserved</span><span class="brand">DEW</span></footer>
</section>

<section class="slide col-l" style="top:4419px">
  <h2 class="slide-title" style="font-size:12px">What are the benefits of having a "Remote Scheduler" within your organization?</h2>
  <div class="panel" style="font-size:8px;line-height:2;padding-top:54px"><ul class="ticks">
    <li>Reduced cost of operation and higher skilled scheduler....bigger bang for your buck!</li>
    <li>Only pay for the amount of work you need</li>
    <li>A lead or master scheduler available when you need them</li>
    <li>A well structured schedule following your company guidelines</li>
    <li>Consistency, your schedules will always be familiar and easy to understand</li>
  </ul></div>
  <footer class="footer"><span class="page">21 &nbsp;|&nbsp; Copyright © 2020 DEW Project Services, Ltd. | All Rights Reserved</span><span class="brand">DEW</span></footer>
</section>
<section class="slide col-r" style="top:4419px">
  <h2 class="slide-title" style="font-size:15px">FREE VECTOR ICON LINKS AVAILABLE</h2>
  <div role="img" aria-label="Grid of blue line vector icons" style="position:absolute;left:24px;top:52px;right:24px;height:210px;background:repeating-linear-gradient(90deg,#dfe5f3 0 14px,#fff 14px 20px),#fff;opacity:.9"></div>
  <footer class="footer"><span class="page">22 &nbsp;|&nbsp; Copyright © 2020 DEW Project Services, Ltd. | All Rights Reserved</span><span class="brand">DEW</span></footer>
</section>

</body>
</html>
```